Providing Back Office Solutions to Financial Advisors and Attorney Needs a Business Card Design

Need a Business Card Design that speaks to Financial Advisor and Attorneys. Some of the word that come to mind is Clean/Simple & Futuristic.

Industry/Entity Type

Business

```html
<!DOCTYPE html>
<html lang="en">
<head>
<meta charset="utf-8">
<title>Kallos Back Office Solutions – Business Card</title>
<link rel="stylesheet" href="https://fonts.googleapis.com/css2?family=Open+Sans:wght@400;600;700&display=swap">
<style>
  :root {
    --backdrop: #a7a7a7;
    --card-light: #ececec;
    --brand-blue: #1a6bab;
    --accent-blue: #1f86c8;
    --tagline-blue: #2d4b9c;
    --ink: #3a3a3a;
    --rule: #7b7b7b;
    --card-blue-deep: #0d5a96;
    --card-blue-glow: #1e8bd0;
    --white: #ffffff;
  }
  * { margin: 0; padding: 0; box-sizing: border-box; }
  html, body {
    width: 1200px; height: 900px; overflow: hidden;
    background: var(--backdrop);
    font-family: "Open Sans", Arial, sans-serif;
  }
  .card {
    position: absolute; top: 170px; width: 347px; height: 561px;
  }
  .card--front { left: 259px; background: var(--card-light); }
  .card--back {
    left: 631px;
    background: radial-gradient(ellipse at 50% 55%, var(--card-blue-glow) 0%, var(--card-blue-deep) 75%);
  }

  .brand { position: absolute; display: flex; align-items: center; gap: 14px; }
  .brand__mark { width: 44px; height: 44px; flex: none; }
  .brand__name {
    font-size: 48px; font-weight: 600; letter-spacing: 3px; line-height: 1;
  }
  .brand__tagline {
    position: absolute; font-size: 16px; letter-spacing: 0.2px; white-space: nowrap;
  }

  .card--front .brand { left: 48px; top: 120px; }
  .card--front .brand__mark { background: var(--brand-blue); }
  .card--front .brand__name { color: var(--brand-blue); }
  .card--front .brand__tagline { left: 106px; top: 183px; color: var(--tagline-blue); }

  .card--back .brand { left: 40px; top: 238px; }
  .card--back .brand__mark { background: var(--white); }
  .card--back .brand__name { color: var(--white); }
  .card--back .brand__tagline { left: 98px; top: 296px; color: var(--white); font-size: 17px; }

  .contact {
    position: absolute; left: 0; right: 0; top: 328px;
    text-align: center; color: var(--ink);
  }
  .contact__name {
    font-size: 23px; font-weight: 400; letter-spacing: 0.5px;
    color: var(--brand-blue); line-height: 1.2;
  }
  .contact__role { font-size: 14.5px; line-height: 1.3; }
  .contact__rule {
    width: 162px; height: 1px; background: var(--rule); margin: 12px auto 13px;
  }
  .contact__line { font-size: 14.5px; line-height: 20px; }
  .contact__label { color: var(--accent-blue); font-weight: 700; }
  .contact__web { color: var(--brand-blue); font-weight: 700; }

  .card__web {
    position: absolute; left: 0; right: 0; top: 490px;
    text-align: center; color: var(--white); font-size: 17px; font-weight: 600;
  }
</style>
</head>
<body>

<section class="card card--front" aria-label="Card front">
  <div class="brand">
    <span class="brand__mark" aria-hidden="true"></span>
    <span class="brand__name">KALLOS</span>
  </div>
  <p class="brand__tagline">BACK OFFICE SOLUTIONS</p>

  <div class="contact">
    <h1 class="contact__name">DANIEL CARTER</h1>
    <p class="contact__role">Managing Director</p>
    <div class="contact__rule"></div>
    <p class="contact__line"><span class="contact__label">P:</span> 044-555 010 200</p>
    <p class="contact__line"><span class="contact__label">E:</span> info@kallosoffice.com</p>
    <p class="contact__line contact__web">www.kallosoffice.com</p>
    <div class="contact__rule"></div>
    <p class="contact__line">12345, Address Goes Here</p>
    <p class="contact__line">Country Name, 123456.</p>
  </div>
</section>

<section class="card card--back" aria-label="Card back">
  <div class="brand">
    <span class="brand__mark" aria-hidden="true"></span>
    <span class="brand__name">KALLOS</span>
  </div>
  <p class="brand__tagline">BACK OFFICE SOLUTIONS</p>
  <p class="card__web">www.kallosoffice.com</p>
</section>

</body>
</html>
```